Garlic Farm for Farm Sales/Restaurant sales

Need a professional, but appealing to agriculture world. We are selling 27 kinds of Organic Garlic from a farm in Simla,CO. I have uploaded logo and business information-we are going to need a template, because I will need to use it for four separate people.
-We are trying to appeal to Farm to table restaurants
-As well as growers/farmers

Target Market(s)

Agriculture Sales/Restaurants-Organic

Industry/Entity Type

Agriculture

Contact Information for Business Card

Want it to look more unique then your average orbel mart card- I want it to look amazing

Font styles to use
Sans Serif

Colors
0455a3
ec1f27
fbed22
ffffff

Requirements
Must have
• Just be creative
Nice to have
• Colorful
Should not have
• plain

```html
<!DOCTYPE html>
<html lang="en">
<head>
<meta charset="utf-8">
<title>Prairie Clove Farm – Business Card</title>
<link rel="stylesheet" href="https://fonts.googleapis.com/css2?family=Source+Sans+3:ital,wght@0,400;0,600;1,400&display=swap">
<style>
  :root {
    --backdrop: #8f8f8f;
    --card-light: #f3f3f3;
    --card-navy: #072850;
    --brand-red: #c8102e;
    --brand-navy: #0b2c5c;
    --text-dark: #1e1e1e;
    --white: #ffffff;
  }
  * { margin: 0; padding: 0; box-sizing: border-box; }
  html, body { width: 1200px; height: 900px; overflow: hidden; }
  body {
    background: var(--backdrop);
    font-family: "Source Sans 3", Arial, sans-serif;
    position: relative;
  }
  .card {
    position: absolute;
    top: 200px;
    width: 310px;
    height: 502px;
  }
  .card--front {
    left: 293px;
    background: var(--card-light);
    border-radius: 48px 0 70px 0;
  }
  .card--back {
    left: 613px;
    width: 309px;
    background: var(--card-navy);
    border-radius: 0 70px 0 48px;
  }
  .brand {
    position: absolute;
    left: 0;
    right: 0;
    display: flex;
    flex-direction: column;
    align-items: center;
  }
  .brand__dot {
    width: 92px;
    height: 92px;
    border-radius: 50%;
    background: var(--brand-red);
  }
  .brand__name {
    margin-top: 22px;
    font-size: 27px;
    font-weight: 600;
    letter-spacing: 0.5px;
    white-space: nowrap;
  }
  .card--front .brand { top: 44px; }
  .card--front .brand__name { color: var(--brand-navy); }
  .card--back .brand { top: 166px; }
  .card--back .brand__name { color: var(--white); }

  .person {
    position: absolute;
    left: 27px;
    top: 280px;
  }
  .person__name {
    color: var(--brand-red);
    font-size: 23px;
    font-weight: 600;
    line-height: 1.1;
  }
  .person__role {
    margin-top: 3px;
    font-size: 14px;
    font-style: italic;
    color: var(--text-dark);
  }
  .contact {
    position: absolute;
    left: 27px;
    top: 346px;
    list-style: none;
  }
  .contact__item {
    display: flex;
    align-items: center;
    height: 18px;
    font-size: 14px;
    color: var(--text-dark);
  }
  .contact__icon {
    width: 11px;
    height: 11px;
    margin-right: 8px;
    fill: var(--brand-red);
    flex: none;
  }
  .address {
    position: absolute;
    left: 27px;
    top: 430px;
    font-size: 14px;
    line-height: 16px;
    color: var(--text-dark);
  }
</style>
</head>
<body>
  <section class="card card--front">
    <div class="brand">
      <div class="brand__dot"></div>
      <div class="brand__name">Prairie Clove Farm</div>
    </div>

    <div class="person">
      <h1 class="person__name">Dana Reyes</h1>
      <p class="person__role">Managing Director</p>
    </div>

    <ul class="contact">
      <li class="contact__item">
        <svg class="contact__icon" viewBox="0 0 12 12"><path d="M1 4c0-2 2-3 5-3s5 1 5 3v1H8V4H4v1H1z M2 6h8l1 5H1z"/></svg>
        555-210-4417
      </li>
      <li class="contact__item">
        <svg class="contact__icon" viewBox="0 0 12 12"><path d="M3 1h6v3H3z M1 5h10v6H1z"/><rect x="3" y="7" width="6" height="1.2" fill="#f3f3f3"/></svg>
        (555)-318-7
      </li>
      <li class="contact__item">
        <svg class="contact__icon" viewBox="0 0 12 12"><path d="M1 2.5h10v7H1z"/><path d="M1 2.5l5 4 5-4" fill="none" stroke="#f3f3f3" stroke-width="1"/></svg>
        hello@prairieclove.com
      </li>
      <li class="contact__item">
        <svg class="contact__icon" viewBox="0 0 12 12"><circle cx="6" cy="6" r="5.5"/><path d="M0.5 6h11 M6 0.5c-2.5 3-2.5 8 0 11 M6 0.5c2.5 3 2.5 8 0 11" fill="none" stroke="#f3f3f3" stroke-width="0.8"/></svg>
        www.prairieclove.com
      </li>
    </ul>

    <address class="address" style="font-style: normal;">
      88 Fieldstone Road<br>
      Simla, CO 80835
    </address>
  </section>

  <section class="card card--back">
    <div class="brand">
      <div class="brand__dot"></div>
      <div class="brand__name">Prairie Clove Farm</div>
    </div>
  </section>
</body>
</html>
```